Outpost Lattice Advisors – Franchise Growth & Development Presentation

Outpost Lattice Advisors is an outsourced franchise sales organization (FSO) that helps franchisors grow their franchise systems without the expense and risk of hiring an internal franchise development team.

We are seeking a professional PowerPoint presentation that will be used to present our services to franchisors, franchise executives, founders, and growth-stage franchise brands.

The presentation should communicate the value of partnering with Outpost Lattice Advisors, including:

• Fractional franchise sales team versus hiring internal staff
• 30+ years of franchise industry experience
• 550+ franchise sales successes
• Immediate access to established franchise broker relationships
• Proven franchise development processes
• Franchise growth strategy and enterprise value creation
• Potential private equity and exit opportunities through franchise expansion

The presentation should feel like a modern consulting, investment, or growth strategy presentation rather than a typical sales brochure. We want strong visual storytelling, custom infographics, professional diagrams, and clean business-oriented design.

The audience includes business owners, franchise founders, franchise executives, and investors who are evaluating growth strategies for their franchise systems.

Target Market(s)

Primary Audience: Emerging franchisors Growth-stage franchise brands Franchise founders Franchise CEOs Franchise presidents Franchise development executives Secondary Audience: Private equity firms Franchise investors Strategic buyers Franchise consultants

Industry/Entity Type

Franchise Development, Private Equity / Business Expansion

Font styles to use
Other font styles liked:
• Use Montserrat for titles and Open Sans for body text.

Requirements
Must have
• Modern professional business design Consistent branding throughout Custom infographics Comparison graphics Broker network ecosystem graphic Enterprise value graphic Easy-to-read charts and visuals Editable PowerPoint format Professional iconography. www.outpostlatticeadvisors.example as reference for colors
Nice to have
• Franchise-related imagery Subtle growth-themed visuals Timeline graphics Data visualization Private equity / valuation style graphics
Should not have
• Cartoon graphics Clip art Overly busy slides Stock-template appearance Bright neon colors Handwritten fonts Excessive text on slides Juvenile or playful design elements

```html
<!DOCTYPE html>
<html lang="en">
<head>
<meta charset="utf-8">
<title>Outpost Lattice Advisors – Franchise Growth Presentation</title>
<link rel="stylesheet" href="https://fonts.googleapis.com/css2?family=Barlow+Semi+Condensed:wght@600;700&family=Barlow:wght@300;400;500;600&display=swap">
<style>
:root{
  --navy:#12305a;
  --navy-deep:#0f2b52;
  --navy-soft:#223a5e;
  --orange:#f39a1f;
  --orange-soft:#f8b25a;
  --ink:#1d2a3a;
  --muted:#6b7480;
  --stage:#8a8a8a;
  --white:#ffffff;
}
*{margin:0;padding:0;box-sizing:border-box}
html,body{width:1200px;height:2671px;overflow:hidden;background:var(--stage)}
.stage{position:absolute;left:0;top:0;width:1158px;height:2578px;transform:scale(1.0363);transform-origin:0 0}
.slide{position:absolute;left:65px;width:1023px;height:575px;background:var(--white);overflow:hidden;font-family:"Barlow",sans-serif;color:var(--ink)}
.slide svg.art{position:absolute;left:0;top:0;width:1023px;height:575px}
.brand{position:absolute;display:flex;align-items:center;gap:6px;font-family:"Barlow Semi Condensed",sans-serif;font-weight:700;font-size:14px;letter-spacing:.3px;color:var(--navy);white-space:nowrap}
.brand::before{content:"";width:8px;height:8px;background:var(--orange)}
.web{position:absolute;font-size:11px;letter-spacing:2.4px;color:var(--muted);white-space:nowrap}
.title{position:absolute;font-family:"Barlow Semi Condensed",sans-serif;font-weight:700;font-size:35px;line-height:45px;color:var(--navy);white-space:nowrap}
.title .accent{color:var(--orange)}
.hero-title{color:var(--white)}
.hero-lede{position:absolute;left:497px;top:377px;width:440px;font-size:15.5px;line-height:21px;font-weight:400;color:var(--white)}
.points{position:absolute;list-style:none}
.points li{display:flex;align-items:center;height:51.5px;font-size:17px;font-weight:400;color:var(--ink);white-space:nowrap}
.points li svg{width:46px;height:50px;margin-right:16px;flex:none}
.points b{color:var(--orange);font-weight:600}
.cost-col{position:absolute}
.cost-col h3{font-family:"Barlow Semi Condensed",sans-serif;font-weight:700;font-size:18px;line-height:23px;color:var(--navy);margin-bottom:14px}
.cost-col h3 span{display:block;color:var(--orange)}
.cost-col ul{list-style:none}
.cost-col li{display:flex;align-items:center;height:30px;font-size:17px;color:var(--ink);white-space:nowrap}
.cost-col li svg{width:20px;height:20px;margin-right:12px;flex:none}
</style>
</head>
<body>
<svg width="0" height="0" style="position:absolute">
  <defs>
    <symbol id="hex" viewBox="0 0 46 50"><path d="M23 2 L43 13.5 V36.5 L23 48 L3 36.5 V13.5 Z" fill="none" stroke="#f39a1f" stroke-width="1.4"/></symbol>
    <symbol id="tick" viewBox="0 0 20 20"><circle cx="10" cy="10" r="8.5" fill="none" stroke="#f39a1f" stroke-width="1.3"/><path d="M6 10.2 L9 13 L14 7.5" fill="none" stroke="#12305a" stroke-width="1.4"/></symbol>
  </defs>
</svg>

<div class="stage">

  <!-- Slide 1: cover -->
  <section class="slide" style="top:57px">
    <svg class="art" viewBox="0 0 1023 575" aria-hidden="true">
      <defs>
        <linearGradient id="meetingTone" x1="0" y1="0" x2="1" y2="1"><stop offset="0" stop-color="#a9b8ab"/><stop offset=".6" stop-color="#8e9c94"/><stop offset="1" stop-color="#dcdfe0"/></linearGradient>
      </defs>
      <rect x="0" y="127" width="1023" height="321" fill="var(--navy)"/>
      <path d="M0 0 H205 L463 283 L195 575 H0 Z" fill="var(--navy)"/>
      <path d="M0 127 H316 L452 276 Q458 283 452 290 L307 448 H0 Z" fill="url(#meetingTone)" role="img" aria-label="Photo: two business partners shaking hands across a meeting table"/>
      <path d="M205 0 L452 271 Q463 283 452 295 L195 575" fill="none" stroke="var(--orange)" stroke-width="7"/>
    </svg>
    <div class="brand" style="left:790px;top:45px">Outpost Lattice Advisors</div>
    <h1 class="title hero-title" style="left:497px;top:149px">Outpost Lattice Advisors<br><span class="accent">Outsourced Franchise<br>Sales &amp; Growth Experts</span></h1>
    <p class="hero-lede">Helping franchisors grow faster without the cost and risk of building an internal franchise development team.</p>
    <div class="web" style="left:737px;top:509px">outpostlatticeadvisors.example</div>
  </section>

  <!-- Slide 2: the challenge -->
  <section class="slide" style="top:678px">
    <svg class="art" viewBox="0 0 1023 575" aria-hidden="true">
      <defs><linearGradient id="teamTone" x1="0" y1="0" x2="1" y2="1"><stop offset="0" stop-color="#e4e6e3"/><stop offset=".5" stop-color="#7d8a99"/><stop offset="1" stop-color="#d8dde2"/></linearGradient></defs>
      <path d="M516 14 Q518 0 532 0 H1023 V182 L712 350 Q690 360 678 340 Z" fill="url(#teamTone)" role="img" aria-label="Photo: team meeting with colleagues shaking hands at a conference table"/>
      <path d="M760 360 L1023 210 V575 H848 L750 398 Q740 372 760 360 Z" fill="var(--navy-soft)"/>
      <path d="M413 575 L690 418 Q712 406 726 428 L815 575 Z" fill="var(--orange-soft)"/>
    </svg>
    <div class="brand" style="left:36px;top:26px">Outpost Lattice Advisors</div>
    <h2 class="title" style="left:90px;top:86px">The Challenge Facing<br><span class="accent">Emerging Franchisors</span></h2>
    <ul class="points" style="left:88px;top:198px">
      <li><svg viewBox="0 0 46 50"><use href="#hex"/><path d="M17 16 V34 M29 16 V34 M13 25 H33" stroke="#12305a" stroke-width="1.2" fill="none"/></svg>Limited franchise sales resources</li>
      <li><svg viewBox="0 0 46 50"><use href="#hex"/><g fill="none" stroke="#12305a" stroke-width="1.2"><circle cx="16" cy="20" r="2.5"/><circle cx="23" cy="20" r="2.5"/><circle cx="30" cy="20" r="2.5"/><path d="M12 33 L16 24 L20 33 M19 33 L23 24 L27 33 M26 33 L30 24 L34 33"/></g></svg>Founder wearing too many hats</li>
      <li><svg viewBox="0 0 46 50"><use href="#hex"/><g fill="none" stroke="#12305a" stroke-width="1.2"><circle cx="23" cy="26" r="8"/><path d="M23 21 V26 L27 28 M15 17 L18 15 M31 17 L28 15"/></g></svg>Inconsistent lead follow-up</li>
      <li><svg viewBox="0 0 46 50"><use href="#hex"/><g fill="none" stroke="#12305a" stroke-width="1.2"><circle cx="23" cy="20" r="4"/><path d="M15 34 Q15 26 23 26 Q31 26 31 34"/></g></svg>Difficulty recruiting franchisees</li>
      <li><svg viewBox="0 0 46 50"><use href="#hex"/><g fill="none" stroke="#12305a" stroke-width="1.2"><circle cx="23" cy="25" r="8"/><path d="M17 31 L29 19"/></g></svg>Lack of broker relationships</li>
      <li><svg viewBox="0 0 46 50"><use href="#hex"/><g fill="none" stroke="#12305a" stroke-width="1.2"><circle cx="23" cy="27" r="7"/><path d="M19 18 L23 14 L27 18 M21 27 H25"/></g></svg>High cost of internal franchise development staff</li>
    </ul>
  </section>

  <!-- Slide 3: why us -->
  <section class="slide" style="top:1300px">
    <svg class="art" viewBox="0 0 1023 575" aria-hidden="true">
      <defs><linearGradient id="officeTone" x1="0" y1="0" x2="1" y2="1"><stop offset="0" stop-color="#c9d2d6"/><stop offset=".5" stop-color="#8a949b"/><stop offset="1" stop-color="#b9c3c7"/></linearGradient></defs>
      <rect width="1023" height="575" fill="url(#officeTone)" role="img" aria-label="Photo: two colleagues reviewing work together on a laptop"/>
      <path d="M640 0 H1023 V575 H640 C470 575 375 430 375 287 C375 140 470 0 640 0 Z" fill="var(--white)"/>
    </svg>
    <div class="brand" style="left:818px;top:20px">Outpost Lattice Advisors</div>
    <h2 class="title" style="left:505px;top:118px">Why Outpost <span class="accent">Lattice Advisors</span></h2>
    <ul class="points" style="left:503px;top:186px">
      <li><svg viewBox="0 0 46 50"><use href="#hex"/><g fill="none" stroke="#12305a" stroke-width="1.2"><circle cx="19" cy="20" r="4"/><circle cx="28" cy="19" r="3.5"/><path d="M12 33 Q12 26 19 26 Q26 26 26 33 M24 25 Q34 23 34 31"/></g></svg>Fractional franchise sales team</li>
      <li><svg viewBox="0 0 46 50"><use href="#hex"/><g fill="none" stroke="#12305a" stroke-width="1.2"><rect x="13" y="16" width="16" height="15"/><path d="M13 21 H29"/><circle cx="29" cy="30" r="5"/><path d="M29 28 V30 H31"/></g></svg><span><b>30+ years</b> franchise industry experience</span></li>
      <li><svg viewBox="0 0 46 50"><use href="#hex"/><path d="M17 15 H29 V35 L23 30 L17 35 Z" fill="none" stroke="#12305a" stroke-width="1.2"/></svg><span><b>550+</b> franchise sales successes</span></li>
      <li><svg viewBox="0 0 46 50"><use href="#hex"/><g fill="none" stroke="#12305a" stroke-width="1.2"><path d="M14 34 V20 L20 16 V34 M20 34 V22 H27 V34 M27 34 V18 L32 20 V34 M12 34 H34"/></g></svg>Immediate execution</li>
      <li><svg viewBox="0 0 46 50"><use href="#hex"/><g fill="none" stroke="#12305a" stroke-width="1.2"><path d="M14 27 Q14 17 23 17 Q32 17 32 27 Z M12 27 H34 M23 14 V17 M15 31 H31"/></g></svg>Proven systems and processes</li>
      <li><svg viewBox="0 0 46 50"><use href="#hex"/><g fill="none" stroke="#12305a" stroke-width="1.2"><path d="M18 21 H15 V35 H31 V21 H28 M23 28 V13 M19 17 L23 13 L27 17"/></g></svg>Deep broker network relationships</li>
    </ul>
    <div class="web" style="left:765px;top:541px">outpostlatticeadvisors.example</div>
  </section>

  <!-- Slide 4: cost comparison -->
  <section class="slide" style="top:1920px">
    <svg class="art" viewBox="0 0 1023 575" aria-hidden="true">
      <defs><linearGradient id="lobbyTone" x1="0" y1="0" x2="1" y2="1"><stop offset="0" stop-color="#e8e6e1"/><stop offset=".55" stop-color="#6f7884"/><stop offset="1" stop-color="#cfd5da"/></linearGradient></defs>
      <path d="M0 80 H545 L602 205 H0 Z" fill="var(--navy)"/>
      <path d="M516 14 Q518 0 532 0 H1023 V208 L728 342 Q706 352 694 332 Z" fill="url(#lobbyTone)" role="img" aria-label="Photo: group of colleagues talking in a bright office lobby"/>
      <path d="M762 362 L1023 215 V575 H852 L752 400 Q742 374 762 362 Z" fill="var(--orange)"/>
    </svg>
    <div class="brand" style="left:36px;top:26px">Outpost Lattice Advisors</div>
    <h2 class="title hero-title" style="left:61px;top:100px;font-size:37px;line-height:38px">The Cost of Hiring<br><span class="accent">vs. Outsourcing</span></h2>
    <div class="cost-col" style="left:65px;top:230px">
      <h3>Internal Franchise<span>Development Director</span></h3>
      <ul>
        <li><svg viewBox="0 0 20 20"><use href="#tick"/></svg>Recruiting costs</li>
        <li><svg viewBox="0 0 20 20"><use href="#tick"/></svg>Salary</li>
        <li><svg viewBox="0 0 20 20"><use href="#tick"/></svg>Benefits</li>
        <li><svg viewBox="0 0 20 20"><use href="#tick"/></svg>Payroll taxes</li>
        <li><svg viewBox="0 0 20 20"><use href="#tick"/></svg>Training</li>
        <li><svg viewBox="0 0 20 20"><use href="#tick"/></svg>Ramp-up period</li>
        <li><svg viewBox="0 0 20 20"><use href="#tick"/></svg>Unknown performance</li>
      </ul>
    </div>
    <div class="cost-col" style="left:316px;top:230px">
      <h3>Outpost Lattice<span>Advisors</span></h3>
      <ul>
        <li><svg viewBox="0 0 20 20"><use href="#tick"/></svg>Fractional investment</li>
        <li><svg viewBox="0 0 20 20"><use href="#tick"/></svg>Entire team of experts</li>
        <li><svg viewBox="0 0 20 20"><use href="#tick"/></svg>Immediate launch</li>
        <li><svg viewBox="0 0 20 20"><use href="#tick"/></svg>Proven processes</li>
        <li><svg viewBox="0 0 20 20"><use href="#tick"/></svg>Existing relationships</li>
        <li><svg viewBox="0 0 20 20"><use href="#tick"/></svg>Scalable growth</li>
      </ul>
    </div>
    <div class="web" style="left:36px;top:544px">outpostlatticeadvisors.example</div>
  </section>

</div>
</body>
</html>
```